Business Card Design Project

I need a business card for an environmentally friendly interior design company called Roomcraft Willow.
I was thinking it might be nice to print the business cards on brown recycled paper with green ink.
In addition to interior design, I will also be able to consult with homeowners regarding their indoor environments and how they might be affecting their health after May 2013 which is when I will complete my certification program. This can be added to the business card at that time: "Certified Habitat Vitalis Dwelling Consultant".
Health

```html
<!DOCTYPE html>
<html lang="en">
<head>
<meta charset="utf-8">
<title>Roomcraft Willow – Business Card Options</title>
<link rel="stylesheet" href="https://fonts.googleapis.com/css2?family=Arimo&family=Roboto+Slab:wght@400&display=swap">
<style>
  :root {
    --board: #ffffff;
    --board-edge: #3a3a3a;
    --heading: #2b2b2b;
    --card: #52381c;
    --band: #2e2119;
    --leaf: #a9c91f;
    --leaf-soft: rgba(169, 201, 31, 0.55);
    --shade: #3a2714;
    --ink-light: #ffffff;
  }
  * { box-sizing: border-box; margin: 0; padding: 0; }
  html, body { width: 1200px; height: 1000px; overflow: hidden; background: var(--board); }
  .board {
    position: relative; width: 1200px; height: 1000px;
    border: 1px solid var(--board-edge); background: var(--board);
  }
  .option-title {
    position: absolute; left: 0; width: 1190px; text-align: center;
    font-family: "Arimo", Arial, sans-serif; font-size: 48px; color: var(--heading);
    font-weight: 400; line-height: 1;
  }
  .card {
    position: absolute; width: 487px; height: 278px; background: var(--card); overflow: hidden;
    font-family: "Roboto Slab", Rockwell, serif;
  }
  .ornament { position: absolute; }
  .ornament--leaf { background: radial-gradient(ellipse at center, var(--leaf) 0%, var(--leaf-soft) 40%, rgba(82,56,28,0) 72%); }
  .ornament--shade { background: radial-gradient(ellipse at center, var(--shade) 0%, rgba(58,39,20,0.6) 45%, rgba(82,56,28,0) 75%); }
  .band { position: absolute; left: 0; top: 111px; width: 100%; height: 56px; background: var(--band); }
  .brand { position: absolute; top: 114px; line-height: 1; }
  .brand__name { font-size: 29px; color: var(--ink-light); letter-spacing: -0.5px; white-space: nowrap; }
  .brand__tagline { font-size: 14.5px; color: var(--leaf); margin-top: 2px; white-space: nowrap; }
  .contact { position: absolute; top: 120px; line-height: 1; }
  .contact__name { font-size: 17px; color: var(--ink-light); }
  .contact__phone { font-size: 16px; color: var(--leaf); margin-top: 5px; }
  .credential { position: absolute; left: 31px; top: 236px; font-size: 12.5px; color: var(--leaf); white-space: nowrap; }
</style>
</head>
<body>
<main class="board">

  <h2 class="option-title" style="top:90px;">option # 01</h2>

  <section class="card card--front" style="left:109px; top:179px;">
    <div class="ornament ornament--leaf" style="left:285px; top:-10px; width:210px; height:125px;" role="img" aria-label="Green floral swirl ornament"></div>
    <div class="ornament ornament--shade" style="left:-10px; top:158px; width:165px; height:110px;" role="img" aria-label="Dark brown floral swirl ornament"></div>
    <div class="ornament ornament--leaf" style="left:398px; top:160px; width:95px; height:90px;" role="img" aria-label="Small green floral swirl ornament"></div>
    <div class="band"></div>
    <div class="brand" style="right:7px; text-align:right;">
      <div class="brand__name">Roomcraft Willow</div>
      <div class="brand__tagline">Environmentally friendly design</div>
    </div>
  </section>

  <section class="card card--back" style="left:617px; top:179px;">
    <div class="ornament ornament--leaf" style="left:-10px; top:-10px; width:200px; height:125px;" role="img" aria-label="Green floral swirl ornament"></div>
    <div class="ornament ornament--shade" style="left:330px; top:148px; width:165px; height:115px;" role="img" aria-label="Dark brown floral swirl ornament"></div>
    <div class="band"></div>
    <div class="contact" style="left:20px;">
      <div class="contact__name">Dana Lee Morrow</div>
      <div class="contact__phone">555-204-7781</div>
    </div>
    <p class="credential">Certified Habitat Vitalis Dwelling Consultant</p>
  </section>

  <h2 class="option-title" style="top:487px;">option # 02</h2>

  <section class="card card--front" style="left:109px; top:570px;">
    <div class="ornament ornament--leaf" style="left:285px; top:-10px; width:210px; height:125px;" role="img" aria-label="Green floral swirl ornament"></div>
    <div class="band"></div>
    <div class="ornament ornament--leaf" style="left:-10px; top:100px; width:148px; height:145px;" role="img" aria-label="Green floral swirl ornament over the band"></div>
    <div class="brand" style="left:134px;">
      <div class="brand__name">Roomcraft Willow</div>
      <div class="brand__tagline">Environmentally friendly design</div>
    </div>
  </section>

  <section class="card card--back" style="left:617px; top:570px;">
    <div class="ornament ornament--leaf" style="left:-10px; top:-10px; width:200px; height:125px;" role="img" aria-label="Green floral swirl ornament"></div>
    <div class="band"></div>
    <div class="ornament ornament--leaf" style="left:338px; top:100px; width:155px; height:145px;" role="img" aria-label="Green floral swirl ornament over the band"></div>
    <div class="contact" style="left:178px;">
      <div class="contact__name">Dana Lee Morrow</div>
      <div class="contact__phone">555-204-7781</div>
    </div>
    <p class="credential">Certified Habitat Vitalis Dwelling Consultant</p>
  </section>

</main>
</body>
</html>
```